Namecard design for Forex trading & training company

We need a design for a financial forex trading company.
Namecard should give customer a professional yet premium feel, able to differentiate from others.
1) most financial companies employs white background, while its clean and professional, it is too mainstream.
2) I am thinking of brown as base colour, however it easily gives the perception of being an Interior Design company
3) Task is to find a design that is able to portray a clean professional feel, at the same time, appear premium and differentiated from others.
*I'll be employing 3D textured print for my company namecard just so as to give it a better finishing.
Please find attached for my logo.
Financial

```html
<!DOCTYPE html>
<html lang="en">
<head>
<meta charset="utf-8">
<title>Veltaris Corporation – Business Card</title>
<link rel="stylesheet" href="https://fonts.googleapis.com/css2?family=Cormorant+Garamond:wght@500&family=Open+Sans:wght@400&display=swap">
<style>
  :root {
    --canvas: #e9e6e2;
    --card-black: #0c0c0e;
    --card-black-soft: #26272b;
    --card-white: #ffffff;
    --accent-violet: #6a5ad8;
    --accent-pink: #c4306a;
    --accent-blue: #5b6fe0;
    --text-light: #e8e8ee;
    --text-muted: #8d90b8;
  }
  * { margin: 0; padding: 0; box-sizing: border-box; }
  html, body {
    width: 1200px; height: 1023px; overflow: hidden;
    background: var(--canvas);
  }
  .stage {
    position: relative; width: 1200px; height: 1023px;
    display: flex; align-items: center; justify-content: center; gap: 60px;
  }
  .card {
    position: relative; width: 500px; height: 286px;
    border-radius: 4px; overflow: hidden;
    box-shadow: 0 14px 30px rgba(0,0,0,0.25);
  }
  .card-front { background: var(--card-white); }
  .card-front .divider { position: absolute; inset: 0; }
  .card-back {
    background: linear-gradient(160deg, var(--card-black) 0%, var(--card-black-soft) 55%, var(--card-black) 100%);
  }
  .wordmark {
    position: absolute; display: flex; align-items: center; gap: 10px;
    white-space: nowrap;
    font-family: "Cormorant Garamond", Georgia, serif; font-weight: 500;
    font-size: 15px; letter-spacing: 4px; text-transform: uppercase;
    color: var(--accent-violet);
  }
  .wordmark .mark {
    width: 12px; height: 12px; border-radius: 50%; flex: none;
    background: var(--accent-violet);
  }
  .card-front .wordmark { top: 28px; right: 36px; }
  .card-back .wordmark {
    top: 50%; left: 50%; transform: translate(-50%, -50%);
    font-size: 19px; letter-spacing: 6px; color: var(--accent-blue);
  }
  .card-back .wordmark .mark { width: 14px; height: 14px; background: var(--accent-blue); }
  .contact-block {
    position: absolute; left: 36px; bottom: 22px;
    font-family: "Open Sans", Arial, sans-serif; color: var(--text-light);
  }
  .person-name {
    font-family: "Cormorant Garamond", Georgia, serif; font-weight: 500;
    font-size: 24px; letter-spacing: 2px; text-transform: uppercase;
    color: var(--accent-blue); line-height: 1;
  }
  .person-title {
    font-size: 11px; letter-spacing: 1px; text-transform: uppercase;
    margin: 4px 0 10px; color: var(--text-light);
  }
  .contact-list { list-style: none; }
  .contact-list li {
    display: flex; align-items: center; gap: 9px;
    font-size: 12.5px; line-height: 21px;
  }
  .contact-list svg { width: 12px; height: 12px; flex: none; }
</style>
</head>
<body>
<main class="stage">
  <section class="card card-front" aria-label="Card front">
    <svg class="divider" viewBox="0 0 500 286" preserveAspectRatio="none" aria-hidden="true">
      <defs>
        <linearGradient id="swoosh" x1="0" x2="1">
          <stop offset="0" stop-color="#6a5ad8"/>
          <stop offset="1" stop-color="#c4306a"/>
        </linearGradient>
        <linearGradient id="gloss" x1="0" y1="0" x2="1" y2="1">
          <stop offset="0" stop-color="#0c0c0e"/>
          <stop offset="0.55" stop-color="#2a2b30"/>
          <stop offset="1" stop-color="#0c0c0e"/>
        </linearGradient>
      </defs>
      <path d="M0,54 C130,50 220,134 330,162 C410,182 470,176 500,166 L500,180 C470,190 410,196 330,176 C220,148 130,64 0,66 Z" fill="url(#swoosh)"/>
      <path d="M0,64 C130,62 220,146 330,174 C410,194 470,188 500,178 L500,286 L0,286 Z" fill="url(#gloss)"/>
    </svg>
    <div class="wordmark"><span class="mark"></span>Veltaris Corporation</div>
    <div class="contact-block">
      <h1 class="person-name">Marcus Lin</h1>
      <p class="person-title">Pantry Manager</p>
      <ul class="contact-list">
        <li>
          <svg viewBox="0 0 12 12"><rect width="12" height="12" rx="2" fill="#8d90b8"/><path d="M3.5 3h1.6l.6 1.6-.9.7a4 4 0 0 0 1.9 1.9l.7-.9 1.6.6V8.5A1 1 0 0 1 8 9.5 5.5 5.5 0 0 1 2.5 4 1 1 0 0 1 3.5 3Z" fill="#0c0c0e"/></svg>
          02105550142
        </li>
        <li>
          <svg viewBox="0 0 12 12"><rect width="12" height="12" rx="2" fill="#8d90b8"/><circle cx="6" cy="6" r="3.3" fill="none" stroke="#0c0c0e" stroke-width="1"/><path d="M2.7 6h6.6M6 2.7c1.4 1.8 1.4 4.8 0 6.6M6 2.7c-1.4 1.8-1.4 4.8 0 6.6" fill="none" stroke="#0c0c0e" stroke-width=".8"/></svg>
          www.brightmarket.co.nz
        </li>
        <li>
          <svg viewBox="0 0 12 12"><rect width="12" height="12" rx="2" fill="#8d90b8"/><rect x="2.5" y="3.5" width="7" height="5" fill="none" stroke="#0c0c0e" stroke-width="1"/><path d="M2.5 3.5 6 6.3l3.5-2.8" fill="none" stroke="#0c0c0e" stroke-width="1"/></svg>
          hello@brightmarket.co.nz
        </li>
      </ul>
    </div>
  </section>

  <section class="card card-back" aria-label="Card back">
    <div class="wordmark"><span class="mark"></span>Veltaris Corporation</div>
  </section>
</main>
</body>
</html>
```